Mesh Banner Design for Business Premises

We require the design of a large mesh banner to be installed across the front fence of our warehouse. The banner should prominently feature our existing Trelborn logo and brand colours (yellow, white, and black) and be designed to be highly visible from the road.

The overall aesthetic should be strong, masculine, and industrial, reflecting the nature of the scaffolding and construction industry. The background should be predominantly black, with our branding incorporated in yellow and white for strong contrast and readability.

The banner should clearly communicate the full scope of services we provide, including:

Scaffold Design
Scaffold Engineering
Scaffold Installation / Erection
Scaffold Dismantling

It should also indicate the types of projects and clients we service, including:

Commercial
Industrial
Residential
Civil

The design should feel bold and professional, with a construction-oriented style that aligns with the scaffolding industry. It should be clean, impactful, and easy to read from a distance, ensuring passing traffic can quickly understand our services.

Where possible, subtle industrial or structural design elements (such as scaffold components, steel textures, or linework) may be incorporated into the background to reinforce the industry theme while keeping the layout uncluttered.

The final design will be produced as a large-format mesh banner for outdoor installation, so it should be created with this application and viewing distance in mind.

```html
<!DOCTYPE html>
<html lang="en">
<head>
<meta charset="utf-8">
<title>Trelborn Mesh Banner</title>
<link href="https://fonts.googleapis.com/css2?family=Barlow+Condensed:wght@600;700&family=Montserrat:ital,wght@0,400;0,700;1,700&display=swap" rel="stylesheet">
<style>
  :root {
    --ink: #0b0c10;
    --navy: #1c2a4a;
    --yellow: #f5a91c;
    --white: #ffffff;
    --paper: #ffffff;
    --text-dark: #14151a;
  }
  * { margin: 0; padding: 0; box-sizing: border-box; }
  html, body { width: 992px; height: 1200px; overflow: hidden; background: var(--paper); }
  body { position: relative; font-family: 'Montserrat', sans-serif; }

  .banner { position: absolute; overflow: hidden; background: var(--ink); color: var(--white); }
  .banner-main { left: 51px; top: 30px; width: 892px; height: 540px; }
  .banner-alt { left: 75px; top: 679px; width: 842px; height: 420px; box-shadow: 0 6px 18px rgba(0,0,0,.35); }

  .backdrop {
    position: absolute; inset: 0;
    background:
      linear-gradient(90deg, rgba(11,12,16,0) 55%, rgba(11,12,16,.75) 100%),
      linear-gradient(180deg, #0d1220 0%, var(--navy) 45%, #111726 75%, var(--ink) 100%);
  }

  .brand { position: absolute; display: flex; align-items: center; }
  .brand-mark { background: var(--yellow); }
  .brand-name { font-family: 'Montserrat', sans-serif; font-weight: 700; color: var(--white); }

  .headline { position: absolute; font-family: 'Barlow Condensed', sans-serif; font-weight: 700; line-height: 1.05; text-transform: uppercase; }
  .headline .accent { color: var(--yellow); }

  .label {
    position: absolute; background: var(--white); color: var(--text-dark);
    font-weight: 700; text-transform: uppercase;
    display: flex; align-items: center; justify-content: center;
    clip-path: polygon(4% 0, 100% 0, 96% 100%, 0 100%);
  }

  .services-row {
    position: absolute; display: flex; align-items: center; justify-content: space-between;
    font-family: 'Barlow Condensed', sans-serif; font-weight: 600;
  }
  .services-row .bar { width: 4px; background: var(--yellow); align-self: stretch; }

  .sectors { position: absolute; display: flex; align-items: center; }
  .sector { font-weight: 700; text-transform: uppercase; text-align: center; line-height: 1.15; }
  .sector-rule { width: 1px; background: var(--yellow); align-self: stretch; }

  .footer { position: absolute; left: 0; right: 0; bottom: 0; background: var(--white); color: var(--text-dark); }
  .footer-contact { position: absolute; right: 0; top: 0; bottom: 0; background: var(--yellow); display: flex; align-items: center; clip-path: polygon(5% 0, 100% 0, 100% 100%, 0 100%); font-weight: 700; text-transform: uppercase; }
  .footer-contact .rule { width: 1px; align-self: stretch; background: var(--text-dark); margin: 8px 0; }

  .checks { position: absolute; list-style: none; }
  .checks li { display: flex; align-items: center; gap: 8px; font-weight: 700; font-size: 13.5px; height: 32px; }
  .checks svg { width: 17px; height: 17px; flex: none; }
</style>
</head>
<body>

  <!-- Main fence banner -->
  <section class="banner banner-main">
    <div class="backdrop" role="img" aria-label="Dark blue photograph of steel scaffolding frames against the sky"></div>

    <div class="brand" style="left:40px; top:88px;">
      <span class="brand-mark" style="width:60px; height:60px;"></span>
      <span class="brand-name" style="font-size:44px; letter-spacing:14px; margin-left:26px;">TRELBORN</span>
    </div>

    <h2 class="headline" style="right:28px; top:150px; font-size:44px; text-align:right;">
      <span class="accent">Strength</span> You<br>Can Rely On
    </h2>

    <div class="label" style="left:54px; top:252px; width:217px; height:34px; font-size:19px;">Our Services</div>

    <div class="services-row" style="left:54px; top:300px; width:810px; height:44px; font-size:35px;">
      <span>Design</span><span class="bar"></span>
      <span>Engineering</span><span class="bar"></span>
      <span>Installation / Erection</span><span class="bar"></span>
      <span>Dismantling</span>
    </div>

    <div class="sectors" style="left:40px; top:398px; width:830px; height:58px; font-size:20px;">
      <span class="sector" style="flex:1.1;">Commercial<br>&amp; Retail</span>
      <span class="sector-rule"></span>
      <span class="sector" style="flex:1.05;">Industrial &amp;<br>Government</span>
      <span class="sector-rule"></span>
      <span class="sector" style="flex:0.8;">Residential<br>&amp; Domestic</span>
      <span class="sector-rule"></span>
      <span class="sector" style="flex:0.95;">Civil &amp;<br>Infrastructure</span>
    </div>

    <footer class="footer" style="height:54px;">
      <span style="position:absolute; left:40px; top:14px; font-size:24px; font-weight:700;">CONTACT NOW</span>
      <span style="position:absolute; left:300px; top:6px; font-size:34px; font-weight:700;">130 055 0148</span>
      <div class="footer-contact" style="left:556px; font-size:16px;">
        <span style="margin-left:38px; margin-right:16px;">1300 5 BUILD</span>
        <span class="rule"></span>
        <span style="margin-left:14px;">TRELBORN.COM.AU</span>
      </div>
    </footer>
  </section>

  <!-- Alternate layout -->
  <section class="banner banner-alt">
    <div class="backdrop" role="img" aria-label="Dark blue photograph of steel scaffolding frames against the sky"></div>

    <div class="brand" style="left:39px; top:55px;">
      <span class="brand-mark" style="width:36px; height:36px;"></span>
      <span class="brand-name" style="font-size:24px; letter-spacing:9px; margin-left:20px;">TRELBORN</span>
    </div>

    <div style="position:absolute; left:457px; top:55px; width:385px; height:32px; background:var(--yellow); clip-path:polygon(4% 0,100% 0,100% 100%,0 100%); display:flex; align-items:center; padding-left:22px; color:var(--text-dark); font-weight:700; font-style:italic; font-size:16.5px;">Safe, Superior Scaffolding Solutions</div>

    <h2 class="headline" style="left:37px; top:158px; font-size:41px;">
      <span class="accent">Strength</span> You<br>Can Rely On
    </h2>

    <div class="label" style="left:332px; top:163px; width:156px; height:26px; font-size:15px;">Our Services</div>

    <ul class="checks" style="left:330px; top:198px;">
      <li><svg viewBox="0 0 20 20"><circle cx="10" cy="10" r="8.8" fill="none" stroke="#f5a91c" stroke-width="1.4"/><path d="M6 10.2l2.8 2.8L14.5 6.6" fill="none" stroke="#f5a91c" stroke-width="1.6"/></svg>Design &amp; Engineering</li>
      <li><svg viewBox="0 0 20 20"><circle cx="10" cy="10" r="8.8" fill="none" stroke="#f5a91c" stroke-width="1.4"/><path d="M6 10.2l2.8 2.8L14.5 6.6" fill="none" stroke="#f5a91c" stroke-width="1.6"/></svg>Steel &amp; Aluminium Systems</li>
    </ul>

    <ul class="checks" style="left:571px; top:166px;">
      <li><svg viewBox="0 0 20 20"><circle cx="10" cy="10" r="8.8" fill="none" stroke="#f5a91c" stroke-width="1.4"/><path d="M6 10.2l2.8 2.8L14.5 6.6" fill="none" stroke="#f5a91c" stroke-width="1.6"/></svg>Erection &amp; Dismantle</li>
      <li><svg viewBox="0 0 20 20"><circle cx="10" cy="10" r="8.8" fill="none" stroke="#f5a91c" stroke-width="1.4"/><path d="M6 10.2l2.8 2.8L14.5 6.6" fill="none" stroke="#f5a91c" stroke-width="1.6"/></svg>Specialised Access Solutions</li>
      <li><svg viewBox="0 0 20 20"><circle cx="10" cy="10" r="8.8" fill="none" stroke="#f5a91c" stroke-width="1.4"/><path d="M6 10.2l2.8 2.8L14.5 6.6" fill="none" stroke="#f5a91c" stroke-width="1.6"/></svg>Mobile Scaffold Hire</li>
    </ul>

    <div class="sectors" style="left:121px; top:306px; width:620px; height:48px; font-size:13.5px;">
      <span class="sector" style="width:141px;">Commercial<br>&amp; Retail</span>
      <span class="sector-rule"></span>
      <span class="sector" style="width:149px;">Industrial &amp;<br>Government</span>
      <span class="sector-rule"></span>
      <span class="sector" style="width:148px;">Residential<br>&amp; Domestic</span>
      <span class="sector-rule"></span>
      <span class="sector" style="flex:1;">Civil &amp;<br>Infrastructure</span>
    </div>

    <footer class="footer" style="height:42px;">
      <span style="position:absolute; left:33px; top:11px; font-size:15.5px;">Servicing <b>Brisbane, Gold Coast &amp; Sunshine Coast</b></span>
      <div class="footer-contact" style="left:457px; font-size:15.5px;">
        <span style="margin-left:37px; margin-right:16px;">1300 5 BUILD</span>
        <span class="rule"></span>
        <span style="margin-left:14px;">TRELBORN.COM.AU</span>
      </div>
    </footer>
  </section>

</body>
</html>
```